Mobile Home Page Design for “Zarvo for Plumbers” – in Figma

PipeDashly: Fast, Reliable Emergency Plumbing at Your Fingertips

PipeDashly is a streamlined platform connecting homeowners with trusted, local plumbers for urgent repairs—whether it’s a burst pipe, leak, or blocked toilet. Designed for speed and peace of mind, our homepage will be clean, modern, and mobile-optimized to guide users from problem to solution in minutes.

Our primary users are homeowners in stressful situations who care most about price transparency and how fast help can arrive. Bookings are made exclusively online, so the user experience must instill confidence and eliminate hesitation.

The call-to-action should be immediate and persuasive—"See Prices & Book" will be prominently featured as the main CTA. Additional trust-builders could include:

A simple 3-step booking illustration (Tell us what’s wrong → See prices → Get a plumber)
Customer reviews or “Trusted by 10,000+ homeowners” badges

Display real-time availability ("Next plumber available in 40 minutes")
Price estimates upfront—with clear service types

Target Market(s)

Home Owners: 35-65 Years old.

Industry/Entity Type

Home Services.

Number of Pages Required

1 page

Font styles to use
Sans Serif

Colors
0054AA
0677BA
7BADD7
CADEEF
E8F1F8
FFF300
FFF600
FEFA6F
FFFEC7
FFFEE8

Requirements
Nice to have
• Map showing that plumbers are nearby. Trustworthy look and feel. Blue/Red or Blue/Yellow.

```html
<!DOCTYPE html>
<html lang="en">
<head>
<meta charset="utf-8">
<title>PipeDashly – Mobile Home Page</title>
<link href="https://fonts.googleapis.com/css2?family=Poppins:wght@400;500;600;700&display=swap" rel="stylesheet">
<style>
:root{
  --backdrop:#141a3a;
  --navy:#1f3580;
  --navy-text:#1e3a8a;
  --brand-blue:#0054aa;
  --mid-blue:#1f5fad;
  --bright-blue:#3b8fe8;
  --soft-blue:#e8f1f8;
  --pale-blue:#cadeef;
  --red:#e0323a;
  --ink:#1b1b1b;
  --grey-text:#5c6470;
  --line:#d6e0ec;
  --white:#ffffff;
}
*{box-sizing:border-box;margin:0;padding:0}
html,body{width:1200px;height:5000px;overflow:hidden}
body{background:var(--backdrop);font-family:'Poppins',sans-serif;position:relative;color:var(--ink)}
.abs{position:absolute}
.screen{position:absolute;overflow:hidden}
.screen-home{left:97px;top:58px;width:430px;height:4903px;background:var(--white)}
.screen-info{left:637px;top:41px;width:429px;height:2100px;background:var(--white)}
.center{text-align:center;left:0;right:0}

/* home header */
.topbar{left:0;top:0;width:430px;height:62px;background:linear-gradient(90deg,#23367e,#2f4ea3)}
.topbar .brand{left:22px;top:16px;color:var(--white);font-size:23px;font-weight:500}
.burger span{position:absolute;right:18px;height:3px;background:var(--white);border-radius:2px}
.availability{left:0;top:62px;width:430px;height:35px;font-size:14px;font-weight:600;color:var(--brand-blue);line-height:35px;text-align:center}
.hero-photo{left:0;top:97px;width:430px;height:553px;background:linear-gradient(160deg,#9aa3ad,#5a6675 55%,#2d3f66)}
.hero-band{left:0;top:650px;width:430px;height:451px;background:var(--soft-blue)}
.hero-card{left:18px;top:377px;width:396px;height:448px;background:var(--white);border-radius:12px;box-shadow:0 4px 14px rgba(0,0,0,.12)}
.hero-card h1{position:absolute;left:0;right:0;top:38px;text-align:center;color:var(--navy-text);font-size:40px;font-weight:600;line-height:46px}
.hero-card p{position:absolute;left:40px;right:40px;top:144px;text-align:center;color:var(--grey-text);font-size:17px;line-height:26px}
.btn-red{left:108px;top:219px;width:179px;height:47px;background:var(--red);color:var(--white);border-radius:24px;font-size:20px;font-weight:500;text-align:center;line-height:47px}
.van{left:78px;top:290px;width:240px;height:150px;border-radius:10px;background:linear-gradient(180deg,#f2f4f7,#c9ced6)}
.trust{width:110px;height:110px;border-radius:50%;top:877px}
.trust-dark{background:#25387f}
.trust-light{background:#49b3e6}
.trust-label{top:1000px;width:140px;text-align:center;color:#2c6bc4;font-size:15px;line-height:21px}

/* services */
.section-title{color:var(--navy-text);font-size:35px;font-weight:600;line-height:44px}
.service-card{left:27px;top:1293px;width:383px;height:481px;border:2px solid #3f6fd0;border-radius:8px;overflow:hidden;background:var(--white)}
.service-photo{left:0;top:0;width:383px;height:266px;background:linear-gradient(135deg,#c8ccd2,#8d97a6 50%,#3e5a9e)}
.service-card h3{position:absolute;left:20px;top:304px;color:var(--navy-text);font-size:29px;font-weight:600}
.service-card p{position:absolute;left:22px;top:352px;right:30px;color:var(--grey-text);font-size:16px;line-height:28px}
.read-more{left:24px;top:437px;color:var(--brand-blue);font-size:17px;font-weight:600;font-style:italic;text-decoration:underline}
.arrow-circle{width:50px;height:50px;border-radius:50%}

/* zarvo band */
.zarvo-band{left:0;top:1854px;width:430px;height:485px;background:linear-gradient(180deg,#3c4fa3,#2e3f8d)}
.light-title{color:var(--white);font-size:30px;font-weight:500;line-height:40px}
.pill{border-radius:26px;color:var(--white);font-size:19px;text-align:center;display:flex;align-items:center;justify-content:center;line-height:25px}
.pill-fill{background:var(--bright-blue)}
.pill-outline{border:2px solid rgba(255,255,255,.85)}
.zarvo-note{top:2252px;color:var(--white);font-size:19px;font-weight:500}

/* call now */
.call-title{left:16px;top:2412px;font-size:30px;font-weight:600;line-height:40px;color:var(--ink)}
.call-sub{left:16px;top:2492px;font-size:14px;color:var(--grey-text)}
.map{left:16px;top:2537px;width:401px;height:200px;background:linear-gradient(135deg,#e9ecef,#d5dbe1)}
.btn-blue{left:16px;top:2758px;width:258px;height:55px;border-radius:28px;background:var(--bright-blue);color:var(--white);font-size:21px;font-weight:500;text-align:center;line-height:55px}

/* why */
.why-band{left:0;top:2885px;width:430px;height:429px;background:linear-gradient(180deg,#2b2e33,#14171b)}
.pill-left{justify-content:flex-start;padding-left:32px}

/* accreditations */
.badge-box{width:190px;height:130px;border:1px solid var(--line);background:var(--white)}
.badge-mark{position:absolute;left:50%;top:50%;transform:translate(-50%,-50%)}

/* areas */
.areas-title{left:18px;top:3717px;font-size:31px;font-weight:600;line-height:40px;color:var(--ink)}
.area{width:190px;height:49px;border:1.5px solid var(--pale-blue);border-radius:5px;font-size:17px;font-weight:600;color:#4a5568;display:flex;align-items:center;padding-left:50px}
.area svg{position:absolute;left:16px;top:12px}
.area-active{background:var(--bright-blue);color:var(--white);border-color:var(--bright-blue)}

/* feedback */
.feedback-band{left:0;top:4437px;width:430px;height:466px;background:var(--soft-blue)}
.feedback-title{top:4472px;font-size:32px;font-weight:600;color:var(--ink)}
.feedback-sub{top:4534px;font-size:16px;line-height:26px;color:var(--grey-text);left:60px;right:60px;text-align:center}
.quote-card{left:35px;top:4591px;width:361px;height:198px;background:var(--white);border-radius:8px}
.avatar{left:148px;top:20px;width:64px;height:64px;border-radius:50%;background:linear-gradient(180deg,#7fb3a0,#3f6f63)}
.quote-text{left:30px;right:30px;top:100px;text-align:center;color:var(--grey-text);font-size:16px;line-height:26px}
.quote-name{left:0;right:0;top:156px;text-align:center;font-size:16px;font-weight:600;color:var(--ink)}

/* faq */
.faq-title{top:66px;font-size:33px;font-weight:600;color:var(--ink)}
.faq-item{left:13px;width:400px;background:#f3f4f6;border-radius:3px}
.faq-item p{position:absolute;left:13px;top:50%;transform:translateY(-50%);width:320px;font-size:16px;line-height:28px;color:var(--ink)}
.faq-item .plus{position:absolute;right:12px;top:50%;margin-top:-17px}
.btn-more{left:108px;top:704px;width:200px;height:53px;border-radius:27px;background:var(--bright-blue);color:var(--white);font-size:20px;font-weight:600;text-align:center;line-height:53px}

/* info */
.info-band{left:0;top:832px;width:429px;height:907px;background:var(--soft-blue)}
.info-brand{left:17px;top:880px;font-size:28px;font-weight:600;color:var(--brand-blue)}
.info-line{left:17px;font-size:16px;color:#555d68}
.info-heading{left:17px;font-size:19px;font-weight:600;color:var(--brand-blue)}
.iso-seal{left:14px;top:1066px;width:100px;height:100px;border-radius:50%;background:var(--navy)}
.iso-caption{left:17px;top:1174px;font-size:19px;font-weight:500;color:var(--ink)}
.social-dot{width:40px;height:40px;border-radius:50%;border:2px solid var(--brand-blue);background:var(--white)}
.store-badge{top:1673px;width:99px;height:29px;border-radius:4px;background:#111;color:var(--white);font-size:11px;text-align:center;line-height:29px}
.legal-band{left:0;top:1739px;width:429px;height:361px;background:var(--mid-blue)}
.legal-text{left:50px;right:50px;top:1778px;text-align:center;color:var(--white);font-size:15px;line-height:22px}
.legal-link{left:0;right:0;text-align:center;color:var(--white);font-size:15px;text-decoration:underline}
.copyright{left:0;right:0;top:2046px;text-align:center;color:var(--white);font-size:15px}
</style>
</head>
<body>

<!-- ===== Home screen ===== -->
<main class="screen screen-home">
  <header class="abs topbar">
    <span class="abs brand">PipeDashly</span>
    <div class="burger">
      <span style="top:20px;width:34px"></span>
      <span style="top:30px;width:28px"></span>
      <span style="top:40px;width:34px"></span>
    </div>
  </header>
  <div class="abs availability">* 12 PLUMBERS ON-CALL NEAR YOU</div>

  <div class="abs hero-photo" role="img" aria-label="Smiling plumber in blue shirt working under a kitchen sink"></div>
  <div class="abs hero-band"></div>

  <section class="abs hero-card">
    <h1>Book A Plumber<br>Near You - Fast</h1>
    <p>Get an instant response from a trusted plumber 24/7</p>
    <div class="abs btn-red">Book Now</div>
    <div class="abs van" role="img" aria-label="White plumbing service van"></div>
  </section>

  <div class="abs trust trust-dark" style="left:21px" role="img" aria-label="Plumber with tools icon"></div>
  <div class="abs trust trust-light" style="left:160px" role="img" aria-label="Certificate document icon"></div>
  <div class="abs trust trust-dark" style="left:306px" role="img" aria-label="Shield held in hands icon"></div>
  <div class="abs trust-label" style="left:6px">Experienced<br>plumbers</div>
  <div class="abs trust-label" style="left:145px">Verified<br>credentials</div>
  <div class="abs trust-label" style="left:291px">Fully insured<br>plumbers</div>

  <h2 class="abs section-title center" style="top:1187px;text-align:center">Services We<br>Provide</h2>
  <article class="abs service-card">
    <div class="abs service-photo" role="img" aria-label="Plumber fitting a kitchen tap against a tiled wall"></div>
    <svg class="abs" style="left:0;top:236px" width="383" height="34" viewBox="0 0 383 34"><polygon points="0,34 0,8 383,0 383,34" fill="#fff"/><polygon points="0,34 0,4 60,0 30,34" fill="#3b8fe8"/></svg>
    <h3>Plumbing</h3>
    <p>We offer all solutions to all your plumbing problems from leaks to blocked toilets</p>
    <span class="abs read-more">Read More</span>
  </article>
  <div class="abs arrow-circle" style="left:377px;top:1425px;background:var(--bright-blue)">
    <svg width="50" height="50" viewBox="0 0 50 50"><path d="M21 16l9 9-9 9" fill="none" stroke="#fff" stroke-width="2.5" stroke-linecap="round"/></svg>
  </div>

  <section class="abs zarvo-band"></section>
  <h2 class="abs light-title center" style="top:1937px;text-align:center">We’re like Zarvo –<br>for Plumbers</h2>
  <div class="abs pill pill-fill" style="left:66px;top:2023px;width:299px;height:48px">Select your issue</div>
  <div class="abs pill pill-outline" style="left:66px;top:2083px;width:299px;height:50px">View our pricing</div>
  <div class="abs pill pill-outline" style="left:66px;top:2141px;width:299px;height:82px">Get an instant<br>response &amp; Book</div>
  <div class="abs zarvo-note center" style="text-align:center">Track your plumber en route to you</div>

  <h2 class="abs call-title">Call an<br>PipeDashly now</h2>
  <p class="abs call-sub">We have plumbers near you ready to assist 24/7.</p>
  <div class="abs map" role="img" aria-label="Street map of London with nearby plumber locations"></div>
  <div class="abs btn-blue">Call a Plumber Now</div>

  <section class="abs why-band" role="img" aria-label="Dark photo of pipework under a sink"></section>
  <h2 class="abs light-title center" style="top:2960px;text-align:center;font-size:31px">Why customers love<br>PipeDashly?</h2>
  <div class="abs pill pill-fill pill-left" style="left:25px;top:3067px;width:381px;height:49px">Select your issue</div>
  <div class="abs pill pill-outline pill-left" style="left:25px;top:3127px;width:381px;height:49px">View our pricing</div>
  <div class="abs pill pill-outline pill-left" style="left:25px;top:3185px;width:381px;height:51px">Get an instant response &amp; Book</div>

  <div class="abs badge-box" style="left:16px;top:3383px"><div class="badge-mark" style="width:150px;height:22px;background:#d61f26"></div></div>
  <div class="abs badge-box" style="left:225px;top:3383px"><div class="badge-mark" style="width:98px;height:104px;background:#111"></div></div>
  <div class="abs badge-box" style="left:16px;top:3527px"><div class="badge-mark" style="width:36px;height:36px;border-radius:50%;background:#2a6fb8"></div></div>
  <div class="abs badge-box" style="left:225px;top:3527px"><div class="badge-mark" style="width:150px;height:60px;border-radius:8px;background:#6a3d8f"></div></div>

  <h2 class="abs areas-title">We’re expanding into all<br>the major boroughs in<br>London &amp; Essex</h2>

  <div class="abs area area-active" style="left:16px;top:3871px"><svg width="18" height="24" viewBox="0 0 18 24"><path d="M9 1a8 8 0 0 1 8 8c0 6-8 14-8 14S1 15 1 9a8 8 0 0 1 8-8z" fill="none" stroke="#fff" stroke-width="2"/><circle cx="9" cy="9" r="3" fill="#fff"/></svg>Barking</div>
  <div class="abs area" style="left:225px;top:3871px"><svg width="18" height="24" viewBox="0 0 18 24"><path d="M9 1a8 8 0 0 1 8 8c0 6-8 14-8 14S1 15 1 9a8 8 0 0 1 8-8z" fill="none" stroke="#3b8fe8" stroke-width="2"/><circle cx="9" cy="9" r="3" fill="#3b8fe8"/></svg>Barnet</div>
  <div class="abs area" style="left:16px;top:3931px"><svg width="18" height="24" viewBox="0 0 18 24"><path d="M9 1a8 8 0 0 1 8 8c0 6-8 14-8 14S1 15 1 9a8 8 0 0 1 8-8z" fill="none" stroke="#3b8fe8" stroke-width="2"/><circle cx="9" cy="9" r="3" fill="#3b8fe8"/></svg>Bexley</div>
  <div class="abs area" style="left:225px;top:3931px"><svg width="18" height="24" viewBox="0 0 18 24"><path d="M9 1a8 8 0 0 1 8 8c0 6-8 14-8 14S1 15 1 9a8 8 0 0 1 8-8z" fill="none" stroke="#3b8fe8" stroke-width="2"/><circle cx="9" cy="9" r="3" fill="#3b8fe8"/></svg>Brent</div>
  <div class="abs area" style="left:16px;top:3991px"><svg width="18" height="24" viewBox="0 0 18 24"><path d="M9 1a8 8 0 0 1 8 8c0 6-8 14-8 14S1 15 1 9a8 8 0 0 1 8-8z" fill="none" stroke="#3b8fe8" stroke-width="2"/><circle cx="9" cy="9" r="3" fill="#3b8fe8"/></svg>Bromley</div>
  <div class="abs area" style="left:225px;top:3991px"><svg width="18" height="24" viewBox="0 0 18 24"><path d="M9 1a8 8 0 0 1 8 8c0 6-8 14-8 14S1 15 1 9a8 8 0 0 1 8-8z" fill="none" stroke="#3b8fe8" stroke-width="2"/><circle cx="9" cy="9" r="3" fill="#3b8fe8"/></svg>Camden</div>
  <div class="abs area" style="left:16px;top:4051px"><svg width="18" height="24" viewBox="0 0 18 24"><path d="M9 1a8 8 0 0 1 8 8c0 6-8 14-8 14S1 15 1 9a8 8 0 0 1 8-8z" fill="none" stroke="#3b8fe8" stroke-width="2"/><circle cx="9" cy="9" r="3" fill="#3b8fe8"/></svg>Croydon</div>
  <div class="abs area" style="left:225px;top:4051px"><svg width="18" height="24" viewBox="0 0 18 24"><path d="M9 1a8 8 0 0 1 8 8c0 6-8 14-8 14S1 15 1 9a8 8 0 0 1 8-8z" fill="none" stroke="#3b8fe8" stroke-width="2"/><circle cx="9" cy="9" r="3" fill="#3b8fe8"/></svg>Ealing</div>
  <div class="abs area" style="left:16px;top:4111px"><svg width="18" height="24" viewBox="0 0 18 24"><path d="M9 1a8 8 0 0 1 8 8c0 6-8 14-8 14S1 15 1 9a8 8 0 0 1 8-8z" fill="none" stroke="#3b8fe8" stroke-width="2"/><circle cx="9" cy="9" r="3" fill="#3b8fe8"/></svg>Enfield</div>
  <div class="abs area" style="left:225px;top:4111px"><svg width="18" height="24" viewBox="0 0 18 24"><path d="M9 1a8 8 0 0 1 8 8c0 6-8 14-8 14S1 15 1 9a8 8 0 0 1 8-8z" fill="none" stroke="#3b8fe8" stroke-width="2"/><circle cx="9" cy="9" r="3" fill="#3b8fe8"/></svg>Greenwich</div>
  <div class="abs area" style="left:16px;top:4171px"><svg width="18" height="24" viewBox="0 0 18 24"><path d="M9 1a8 8 0 0 1 8 8c0 6-8 14-8 14S1 15 1 9a8 8 0 0 1 8-8z" fill="none" stroke="#3b8fe8" stroke-width="2"/><circle cx="9" cy="9" r="3" fill="#3b8fe8"/></svg>Hackney</div>
  <div class="abs area" style="left:225px;top:4171px"><svg width="18" height="24" viewBox="0 0 18 24"><path d="M9 1a8 8 0 0 1 8 8c0 6-8 14-8 14S1 15 1 9a8 8 0 0 1 8-8z" fill="none" stroke="#3b8fe8" stroke-width="2"/><circle cx="9" cy="9" r="3" fill="#3b8fe8"/></svg>Haringey</div>
  <div class="abs area" style="left:16px;top:4231px"><svg width="18" height="24" viewBox="0 0 18 24"><path d="M9 1a8 8 0 0 1 8 8c0 6-8 14-8 14S1 15 1 9a8 8 0 0 1 8-8z" fill="none" stroke="#3b8fe8" stroke-width="2"/><circle cx="9" cy="9" r="3" fill="#3b8fe8"/></svg>Harrow</div>
  <div class="abs area" style="left:225px;top:4231px"><svg width="18" height="24" viewBox="0 0 18 24"><path d="M9 1a8 8 0 0 1 8 8c0 6-8 14-8 14S1 15 1 9a8 8 0 0 1 8-8z" fill="none" stroke="#3b8fe8" stroke-width="2"/><circle cx="9" cy="9" r="3" fill="#3b8fe8"/></svg>Havering</div>

  <svg class="abs" style="left:159px;top:4315px" width="112" height="50" viewBox="0 0 112 50">
    <circle cx="25" cy="25" r="24" fill="#3b8fe8"/><path d="M29 16l-9 9 9 9" fill="none" stroke="#fff" stroke-width="2.5" stroke-linecap="round"/>
    <circle cx="87" cy="25" r="23" fill="#fff" stroke="#3b8fe8" stroke-width="2"/><path d="M83 16l9 9-9 9" fill="none" stroke="#3b8fe8" stroke-width="2.5" stroke-linecap="round"/>
  </svg>

  <section class="abs feedback-band"></section>
  <h2 class="abs feedback-title center" style="text-align:center">Customer feedback</h2>
  <p class="abs feedback-sub">We serve customers instantly across the whole of London.</p>
  <article class="abs quote-card">
    <div class="abs avatar" role="img" aria-label="Customer portrait"></div>
    <p class="abs quote-text">Was here in under 15 minutes to fix my leak at midnight!</p>
    <p class="abs quote-name">Maya, Shoreditch</p>
  </article>
  <svg class="abs" style="left:85px;top:4816px" width="260" height="50" viewBox="0 0 260 50">
    <line x1="0" y1="25" x2="48" y2="25" stroke="#7badd7" stroke-width="1.5"/>
    <line x1="212" y1="25" x2="260" y2="25" stroke="#7badd7" stroke-width="1.5"/>
    <circle cx="74" cy="25" r="24" fill="#0054aa"/><path d="M78 16l-9 9 9 9" fill="none" stroke="#fff" stroke-width="2.5" stroke-linecap="round"/>
    <circle cx="186" cy="25" r="23" fill="#fff" stroke="#0054aa" stroke-width="2"/><path d="M182 16l9 9-9 9" fill="none" stroke="#0054aa" stroke-width="2.5" stroke-linecap="round"/>
  </svg>
</main>

<!-- ===== FAQ & footer screen ===== -->
<aside class="screen screen-info">
  <h2 class="abs faq-title center" style="text-align:center">Faq’s</h2>

  <div class="abs faq-item" style="top:137px;height:80px"><p>How can you verify that PipeDashly are reliable?</p><svg class="plus" width="34" height="34" viewBox="0 0 34 34"><circle cx="17" cy="17" r="17" fill="#3b8fe8"/><path d="M17 10v14M10 17h14" stroke="#fff" stroke-width="3"/></svg></div>
  <div class="abs faq-item" style="top:227px;height:77px"><p>Are your plumbers registered with GasSure?</p><svg class="plus" width="34" height="34" viewBox="0 0 34 34"><circle cx="17" cy="17" r="17" fill="#3b8fe8"/><path d="M17 10v14M10 17h14" stroke="#fff" stroke-width="3"/></svg></div>
  <div class="abs faq-item" style="top:316px;height:78px"><p>Do your plumbers have insurance?</p><svg class="plus" width="34" height="34" viewBox="0 0 34 34"><circle cx="17" cy="17" r="17" fill="#3b8fe8"/><path d="M17 10v14M10 17h14" stroke="#fff" stroke-width="3"/></svg></div>
  <div class="abs faq-item" style="top:405px;height:78px"><p>How much do your plumbers cost?</p><svg class="plus" width="34" height="34" viewBox="0 0 34 34"><circle cx="17" cy="17" r="17" fill="#3b8fe8"/><path d="M17 10v14M10 17h14" stroke="#fff" stroke-width="3"/></svg></div>
  <div class="abs faq-item" style="top:495px;height:77px"><p>Do you charge a call-out fee?</p><svg class="plus" width="34" height="34" viewBox="0 0 34 34"><circle cx="17" cy="17" r="17" fill="#3b8fe8"/><path d="M17 10v14M10 17h14" stroke="#fff" stroke-width="3"/></svg></div>
  <div class="abs faq-item" style="top:584px;height:78px"><p>What plumbing services do PipeDashly offer?</p><svg class="plus" width="34" height="34" viewBox="0 0 34 34"><circle cx="17" cy="17" r="17" fill="#3b8fe8"/><path d="M17 10v14M10 17h14" stroke="#fff" stroke-width="3"/></svg></div>
  <div class="abs btn-more">MORE FAQ’s</div>

  <section class="abs info-band"></section>
  <div class="abs info-brand">PipeDashly</div>
  <p class="abs info-line" style="top:930px">Created with in London</p>
  <p class="abs info-line" style="top:958px">Registered in England and Wales</p>
  <p class="abs info-line" style="top:986px">Company Number 999888877</p>
  <p class="abs info-line" style="top:1014px">ICO Registration AB9876543</p>
  <div class="abs iso-seal" role="img" aria-label="Information security certification seal"></div>
  <p class="abs iso-caption">ISO27001 Compliant</p>

  <h3 class="abs info-heading" style="top:1232px">Address</h3>
  <svg class="abs" style="left:15px;top:1276px" width="40" height="40" viewBox="0 0 40 40"><circle cx="20" cy="20" r="19" fill="#fff" stroke="#0054aa" stroke-width="1.5"/><path d="M20 10a7 7 0 0 1 7 7c0 5-7 13-7 13s-7-8-7-13a7 7 0 0 1 7-7z" fill="none" stroke="#0054aa" stroke-width="2"/><circle cx="20" cy="17" r="2.5" fill="#0054aa"/></svg>
  <p class="abs info-line" style="left:74px;top:1276px;line-height:24px">212 Harbour Lane London,<br>SE4 7QX, UK.</p>

  <h3 class="abs info-heading" style="top:1358px">DISCOVER</h3>
  <p class="abs info-line" style="top:1392px">Blog Title 1</p>
  <p class="abs info-line" style="top:1421px">Blog Title 2</p>
  <p class="abs info-line" style="top:1450px">Blog Title 3</p>
  <p class="abs info-line" style="top:1479px">Blog Title 4</p>
  <p class="abs info-line" style="top:1508px">Blog Title 2 on two lines</p>

  <h3 class="abs info-heading" style="top:1566px">SOCIAL</h3>
  <div class="abs social-dot" style="left:15px;top:1606px"></div>
  <div class="abs social-dot" style="left:61px;top:1606px"></div>
  <div class="abs social-dot" style="left:110px;top:1606px"></div>
  <div class="abs social-dot" style="left:156px;top:1606px"></div>
  <div class="abs store-badge" style="left:15px">App Download</div>
  <div class="abs store-badge" style="left:122px">App Download</div>

  <section class="abs legal-band"></section>
  <p class="abs legal-text">PipeDashly.co.uk is a trading name of Pipewell Holdings Ltd, registered at Companies House in England and Wales under company registration number 8987889.</p>
  <a class="abs legal-link" style="top:1899px">Privacy and Cookie Policy</a>
  <a class="abs legal-link" style="top:1925px">Terms &amp; Conditions</a>
  <a class="abs legal-link" style="top:1951px">Service Terms &amp; Conditions</a>
  <a class="abs legal-link" style="top:1977px">Complaints Policy</a>
  <a class="abs legal-link" style="top:2003px">Other Policy</a>
  <p class="abs copyright">© Pipewell Holdings Ltd. All Rights Reserved.</p>
</aside>

</body>
</html>
```